Bright Harbor Real Estate Institute

This must be done in word press and I will need about 7 tabs The home page, Information page, Schedule and Cost page which will link to a Email me form, a online registration a about us and location/contact tab Each tab will then open several other pages. The home page will describe different courses that we offer since all the schools are about the same you can get a good ideal by going to qelvanto.org or pinnaclebayrealtyschool.com and looking at their site I would like mine to be similar as the courses are exactly the same but I would like the site to be more modern I also need it to be in word press so I can change it and update the dates as they change I have attached he logo below

Target Market(s)

people interested in getting into real estate and those who need continuing education

Coding

Coded - Design and coding required

Number of Pages Required

5+ page

Font styles to use
Sans Serif

Colors
3276b5

Requirements
Must have
• A page to schedule classes, a tab so the college I am partnering with can link the online courses to the back side, a page that describes the type of classes I offer

```html
<!DOCTYPE html>
<html lang="en">
<head>
<meta charset="utf-8">
<title>Bright Harbor Real Estate Institute</title>
<link href="https://fonts.googleapis.com/css2?family=Montserrat:wght@400;500;600;700;800&display=swap" rel="stylesheet">
<style>
:root{
  --brand:#3276b5;
  --brand-dark:#2b63a0;
  --accent:#f5c518;
  --ink:#333a45;
  --muted:#5b6472;
  --page:#f5f7fa;
  --slab:#e1e7f0;
  --hex:#d8dfe9;
  --card:#e6ebf3;
  --band:#2c3a9e;
  --band-card:#252f86;
  --footer:#262a58;
  --footer-box:#1d2150;
  --white:#fff;
}
*{margin:0;padding:0;box-sizing:border-box}
html,body{width:961px;height:1200px;overflow:hidden}
body{position:relative;background:var(--page);font-family:'Montserrat',sans-serif;color:var(--ink)}
.abs{position:absolute}

.site-header{left:0;top:0;width:961px;height:36px;background:var(--white);z-index:3;box-shadow:0 1px 3px rgba(0,0,0,.08)}
.brand{left:181px;top:7px;width:95px;color:var(--brand);font-weight:700;font-size:7.5px;line-height:9px;text-transform:uppercase}
.main-nav{left:300px;top:11px;display:flex;gap:12px;font-size:8.5px;font-weight:500;color:#3d4450}
.header-divider{left:684px;top:7px;width:1px;height:19px;background:#d4d8de}
.phone-icon{left:695px;top:9px}
.service{left:715px;top:7px;line-height:10px}
.service small{display:block;font-size:6px;font-weight:600;color:var(--brand)}
.service b{font-size:8.5px;font-weight:500;color:#2a2f38}

.hero-photo{left:0;top:36px;width:961px;height:243px;background:linear-gradient(180deg,#9fc0e0 0%,#cfdfee 40%,#8ea1b8 70%,#4d5a6c 100%)}
.courses-panel{left:180px;top:238px;width:600px;height:60px;background:var(--page)}

.backdrop{left:0;top:0;z-index:0}
.section-title{left:0;width:961px;text-align:center;font-weight:800;color:var(--brand);font-size:16px}
.intro{left:290px;top:278px;width:381px;text-align:center;font-size:8.5px;line-height:12px;color:var(--muted)}

.course{top:322px;width:158px;height:227px;background:var(--card);box-shadow:0 14px 10px -12px rgba(60,80,110,.25)}
.course.featured{background:var(--brand)}
.course-photo{width:158px;height:99px}
.course-tag{position:absolute;left:22px;top:113px;font-size:6.3px;font-weight:700;color:var(--brand)}
.course-name{position:absolute;left:22px;top:129px;width:125px;font-size:9.5px;line-height:11px;font-weight:700;color:#2d333d}
.course-desc{position:absolute;left:22px;top:159px;width:120px;font-size:7.4px;line-height:11px;color:var(--muted)}
.course.featured .course-tag{color:var(--accent)}
.course.featured .course-name,.course.featured .course-desc{color:var(--white)}
.btn{position:absolute;display:flex;align-items:center;justify-content:center;border-radius:11px;background:var(--brand);color:var(--white);font-size:7px;font-weight:600}
.btn::after{content:"›";font-size:11px;position:absolute;right:10px;top:2px}
.course .btn{left:21px;top:192px;width:115px;height:20px}
.course.featured .btn{background:var(--white);color:#2d333d}
.carousel-arrow{top:425px;z-index:2}

.feature{width:105px;height:79px;background:var(--white);box-shadow:0 2px 6px rgba(60,80,110,.12);border-radius:2px;z-index:2;padding:16px 0 0 17px}
.feature.active{background:var(--brand)}
.feature h3{font-size:8.5px;font-weight:700;color:var(--brand);margin-top:5px}
.feature.active h3{color:var(--accent)}
.feature p{font-size:6px;font-weight:500;line-height:8px;color:#3a4250;margin-top:3px;width:75px}
.feature.active p{color:var(--white)}
.about-heading{right:233px;top:669px;width:240px;text-align:right;font-size:16.5px;line-height:18px;font-weight:700;color:var(--brand);z-index:2}
.about-text{right:233px;top:718px;width:205px;text-align:right;font-size:8.4px;line-height:12px;color:var(--muted);z-index:2}
.contact-btn{left:654px;top:813px;width:75px;height:20px;z-index:2;justify-content:flex-start;padding-left:10px}
.contact-btn.btn::after{right:9px}

.testimonials{left:0;top:904px;width:961px;height:256px;background:var(--band)}
.t-title{top:932px;color:var(--white);font-size:16.5px;font-weight:700}
.t-sub{left:0;top:961px;width:961px;text-align:center;color:var(--white);font-size:8.5px;font-weight:500}
.quote{width:259px;height:113px;top:1003px;background:var(--band-card);box-shadow:0 14px 10px -12px rgba(10,15,60,.45)}
.avatar{width:54px;height:54px;border-radius:50%;border:2px solid var(--white);top:1033px;background:linear-gradient(160deg,#c9b2a1,#6b5546)}
.quote-name{color:var(--white);font-size:11px;font-weight:700;top:1020px}
.quote-text{color:#dfe3ff;font-size:8.4px;line-height:12px;top:1041px;width:175px}
.quote-mark{font-family:'Montserrat',sans-serif;font-weight:800;font-size:62px;color:var(--brand);line-height:1}

.site-footer{left:0;top:1160px;width:961px;height:40px;background:var(--footer)}
.footer-service{left:180px;top:1166px;width:93px;height:29px;background:var(--footer-box);border-radius:2px}
.footer-service .txt{position:absolute;left:26px;top:6px;line-height:8px;color:var(--white)}
.footer-service small{display:block;font-size:5.8px;font-weight:600}
.footer-service b{font-size:8px;font-weight:500}
.footer-nav{left:330px;top:1177px;display:flex;gap:19px;font-size:6.3px;font-weight:600;color:#cfd3ea}
.footer-brand{left:715px;top:1172px;width:66px;font-size:5.8px;line-height:7px;font-weight:700;color:#8b93c4;text-transform:uppercase;text-align:right}
</style>
</head>
<body>

<svg class="abs backdrop" width="961" height="1200" viewBox="0 0 961 1200" aria-hidden="true">
  <polygon points="0,618 445,682 961,461 961,904 0,904" fill="var(--slab)"/>
  <polygon points="305,587 431,657 431,801 305,872 181,801 181,657" fill="var(--hex)"/>
  <polygon points="341,591 200,628 165,767 268,868 423,829" fill="none" stroke="#a9bfd8" stroke-width="0.8"/>
  <line x1="341" y1="591" x2="423" y2="660" stroke="#a9bfd8" stroke-width="0.8"/>
</svg>

<header class="abs site-header">
  <div class="abs brand">Bright Harbor Real Estate Institute</div>
  <nav class="abs main-nav"><span>Home</span><span>Information</span><span>Schedule &amp; Cost</span><span>Registration</span><span>About us</span><span>Contact</span></nav>
  <div class="abs header-divider"></div>
  <svg class="abs phone-icon" width="13" height="13" viewBox="0 0 24 24" aria-hidden="true"><path fill="var(--brand)" d="M6.6 10.8a15 15 0 0 0 6.6 6.6l2.2-2.2c.3-.3.7-.4 1-.2 1.1.4 2.3.6 3.6.6.6 0 1 .4 1 1V20c0 .6-.4 1-1 1A17 17 0 0 1 3 4c0-.6.4-1 1-1h3.5c.6 0 1 .4 1 1 0 1.3.2 2.5.6 3.6.1.3 0 .7-.2 1z"/></svg>
  <div class="abs service"><small>Customer Service</small><b>000-000-0000</b></div>
</header>

<div class="abs hero-photo" role="img" aria-label="Aerial view of a city skyline with skyscrapers under a cloudy sky"></div>
<div class="abs courses-panel"></div>

<h2 class="abs section-title" style="top:253px">Our courses</h2>
<p class="abs intro">Lorem ipsum dolor sit amet, consectetur adipisicing elit, sed do eiusmod tempor incididunt ut labore et dolore magna aliqua. Ut enim ad minim veniam, quis nostrud</p>

<svg class="abs carousel-arrow" style="left:199px" width="16" height="22" viewBox="0 0 16 22" aria-hidden="true"><polyline points="12,2 3,11 12,20" fill="none" stroke="#9fc0e0" stroke-width="3"/></svg>
<svg class="abs carousel-arrow" style="left:746px" width="16" height="22" viewBox="0 0 16 22" aria-hidden="true"><polyline points="4,2 13,11 4,20" fill="none" stroke="#9fc0e0" stroke-width="3"/></svg>

<article class="abs course" style="left:232px">
  <div class="course-photo" role="img" aria-label="City skyline with a tall tower at dusk" style="background:linear-gradient(180deg,#aab7c7 0%,#c9c3cc 45%,#4e5966 100%)"></div>
  <span class="course-tag">Continuing Education</span>
  <h3 class="course-name">Buyer Representation<br>in Real Estate</h3>
  <p class="course-desc">This course offers a great intro-duction for buyer agents.</p>
  <span class="btn">Schedule course</span>
</article>
<article class="abs course featured" style="left:402px">
  <div class="course-photo" role="img" aria-label="Forested mountain valley in sunlight" style="background:linear-gradient(180deg,#8ea6b6 0%,#6d8a6c 45%,#2f5220 100%)"></div>
  <span class="course-tag">Continuing Education</span>
  <h3 class="course-name" style="width:132px">Environmental Issues in Your Real Estate Practice</h3>
  <p class="course-desc">This course offers a great intro-duction for buyer agents.</p>
  <span class="btn">Schedule course</span>
</article>
<article class="abs course" style="left:571px">
  <div class="course-photo" role="img" aria-label="Smiling woman on a phone holding a laptop outdoors" style="background:linear-gradient(120deg,#56604a 0%,#a89a7a 55%,#e3d2b6 100%)"></div>
  <span class="course-tag">Continuing Education</span>
  <h3 class="course-name">Introduction to Real<br>Estate Sales</h3>
  <p class="course-desc">This course offers a great intro-duction for buyer agents.</p>
  <span class="btn">Schedule course</span>
</article>

<div class="abs feature" style="left:232px;top:648px">
  <svg width="8" height="12" viewBox="0 0 8 12" aria-hidden="true"><circle cx="5" cy="1.6" r="1.5" fill="var(--brand)"/><path d="M2 5h4l-1.5 6H6v1H1v-1h1.5L3.7 6H2z" fill="var(--brand)"/></svg>
  <h3>Information</h3><p>Lorem ipsum dolor sit amet, consectetur</p>
</div>
<div class="abs feature active" style="left:346px;top:670px">
  <svg width="12" height="12" viewBox="0 0 12 12" aria-hidden="true"><circle cx="6" cy="6" r="5.2" fill="none" stroke="#fff" stroke-width="1"/><path d="M6 3v3.3h2.3" fill="none" stroke="#fff" stroke-width="1"/></svg>
  <h3>Schedule &amp; Cost</h3><p>Lorem ipsum dolor sit amet, consectetur</p>
</div>
<div class="abs feature" style="left:232px;top:736px">
  <svg width="12" height="12" viewBox="0 0 12 12" aria-hidden="true"><rect width="12" height="12" rx="1.5" fill="var(--brand)"/><g fill="#fff"><rect x="2.5" y="3" width="1.3" height="1.2"/><rect x="5" y="3" width="4.5" height="1.2"/><rect x="2.5" y="5.4" width="1.3" height="1.2"/><rect x="5" y="5.4" width="4.5" height="1.2"/><rect x="2.5" y="7.8" width="1.3" height="1.2"/><rect x="5" y="7.8" width="4.5" height="1.2"/></g></svg>
  <h3>Registration</h3><p>Lorem ipsum dolor sit amet, consectetur</p>
</div>
<div class="abs feature" style="left:346px;top:757px">
  <svg width="15" height="12" viewBox="0 0 15 12" aria-hidden="true"><path d="M7.5 1 15 4.5 7.5 8 0 4.5z" fill="var(--brand)"/><path d="M3 6.5v3c1.5 1.6 7.5 1.6 9 0v-3L7.5 8.6z" fill="var(--brand)"/></svg>
  <h3>Courses</h3><p>Lorem ipsum dolor sit amet, consectetur</p>
</div>

<h2 class="abs about-heading">Lorem ipsum dolor sit amet, consectetur adip-</h2>
<p class="abs about-text">Lorem ipsum dolor sit amet, consectetur adip-isicing elit, sed do eiusmod tempor incididunt ut labore et dolore magna aliqua. Ut enim ad minim veniam, quis nostrud exercitation ullam-co laboris nisi ut aliquip ex ea commodo conse-quat. Duis aute irure dolor in reprehenderit in</p>
<span class="btn contact-btn abs">Contact us</span>

<section class="abs testimonials"></section>
<h2 class="abs section-title t-title">Testimonial</h2>
<p class="abs t-sub">What our students talk abou us.</p>

<div class="abs quote" style="left:203px"></div>
<span class="abs quote-mark" style="left:195px;top:990px">“</span>
<span class="abs quote-mark" style="left:434px;top:1093px">”</span>
<div class="abs avatar" role="img" aria-label="Portrait of a smiling student" style="left:192px"></div>
<h3 class="abs quote-name" style="left:263px">Lena Varga</h3>
<p class="abs quote-text" style="left:263px">Lorem ipsum dolor sit amet, consectetur adipisicing elit, sed do eiusmod tempor incididunt ut labore et dolore magna aliqua. Ut enim ad minim veniam, quis nostrud exercitation ullamco laboris nisi</p>

<div class="abs quote" style="left:506px"></div>
<span class="abs quote-mark" style="left:498px;top:990px">“</span>
<span class="abs quote-mark" style="left:737px;top:1093px">”</span>
<div class="abs avatar" role="img" aria-label="Portrait of a male student" style="left:495px;background:linear-gradient(160deg,#d9dbe0,#4b4a4e)"></div>
<h3 class="abs quote-name" style="left:566px">Marcus T.</h3>
<p class="abs quote-text" style="left:566px">Lorem ipsum dolor sit amet, consectetur adipisicing elit, sed do eiusmod tempor incididunt ut labore et dolore magna aliqua. Ut enim ad minim veniam, quis nostrud exercitation ullamco laboris nisi</p>

<footer class="abs site-footer"></footer>
<div class="abs footer-service">
  <svg class="abs" style="left:7px;top:8px" width="13" height="13" viewBox="0 0 24 24" aria-hidden="true"><path fill="#fff" d="M6.6 10.8a15 15 0 0 0 6.6 6.6l2.2-2.2c.3-.3.7-.4 1-.2 1.1.4 2.3.6 3.6.6.6 0 1 .4 1 1V20c0 .6-.4 1-1 1A17 17 0 0 1 3 4c0-.6.4-1 1-1h3.5c.6 0 1 .4 1 1 0 1.3.2 2.5.6 3.6.1.3 0 .7-.2 1z"/></svg>
  <div class="txt"><small>Customer Service</small><b>000-000-0000</b></div>
</div>
<nav class="abs footer-nav"><span>Home</span><span>Information</span><span>Schedule &amp; Cost</span><span>Registration</span><span>About us</span><span>Contact</span></nav>
<div class="abs footer-brand">Bright Harbor Real Estate Institute</div>

</body>
</html>
```